Webdesign teambuilding site Velumo.be with shopping cart

The website www.velumo.be needs a redesign. Velumo offers teambuildings and our mascotte is a chimpansee. Attached is our logo where you can take the monkey from.
We would like to have a startpage design and a concept detail page like https://www.velumo.be/teambuilding-activiteit/drum-rush.
In the design we prefer a fresh, joyfull and modern design. The current website needs a refreshment, I believe to look and feel can remain similar. Of course a complete redesign in line with our logo is also possible.
The colors can be picked from the logo. The green is #afca0a, the dark grey is #504f4f and the light grey is #646463.
In the new website we will also include a shopping basket. Can you also include this in the design?

Target Market(s)

Mainly companies, but also families, friends, ...

Industry/Entity Type

Teambuilding activities

Number of Pages Required

2 page

Font styles to use
Other font styles liked:
• Eurostile

Colors
59FF00
82FF00
B8FF75
E3FFCB
F4FFEA

Requirements
Must have
• Different design elements to stimulate scrolling. Some page become very long and we try to keep the visitors attention
Nice to have
• The reservation page on https://erp.velumo.be/widget will also be redesigned
Should not have
• Rectangular blocks that makes the design looks like a table

```html
<!DOCTYPE html>
<html lang="nl">
<head>
<meta charset="utf-8">
<title>Velumo – Teambuilding met een twist</title>
<link href="https://fonts.googleapis.com/css2?family=Michroma&family=Inter:ital,wght@0,400;0,600;1,400&display=swap" rel="stylesheet">
<style>
:root{
  --green:#afca0a;
  --green-soft:#e3efb0;
  --mint:#f4f8e4;
  --dark:#504f4f;
  --grey:#646463;
  --paper:#f5f5f3;
  --ink:#3b3b3b;
  --white:#ffffff;
  --head:'Michroma',sans-serif;
  --body:'Inter',sans-serif;
}
*{box-sizing:border-box;margin:0;padding:0}
html,body{width:1058px;height:1200px;overflow:hidden;background:var(--white)}
body{font-family:var(--body);color:var(--ink)}
.stage{position:absolute;left:0;top:0;width:1803px;height:2044px;transform:scale(.5868);transform-origin:0 0}
.abs{position:absolute}
.screen{position:absolute;top:0;width:601px;overflow:hidden;background:var(--white)}
h1,h2,h3,.head{font-family:var(--head);font-weight:400}

.nav{position:absolute;left:0;top:0;width:601px;height:37px;background:var(--white)}
.brand{position:absolute;left:7px;top:6px;width:67px;height:24px;background:var(--dark);color:var(--white);font-family:var(--head);font-size:9px;display:flex;align-items:center;justify-content:center;letter-spacing:.5px}
.nav-links{position:absolute;left:195px;top:13px;display:flex;gap:15px;font-family:var(--head);font-size:7.5px;color:var(--grey)}
.nav-lang{position:absolute;left:553px;top:13px;font-size:7.5px;color:var(--grey)}
.nav-cart{position:absolute;left:586px;top:12px}

.hero{position:absolute;left:0;width:601px}
.hero-photo{position:absolute;inset:0}
.hero-title{position:absolute;left:0;width:601px;text-align:center;color:var(--white);font-size:34px;line-height:33px}
.pill{display:inline-flex;align-items:center;justify-content:center;border-radius:20px;background:var(--green);color:var(--white);font-family:var(--head);font-size:8.5px;letter-spacing:.6px;white-space:nowrap}

.section-title{position:absolute;left:0;width:601px;text-align:center;font-size:23px;color:var(--dark)}
.feature{position:absolute;width:225px;height:69px;background:var(--mint);border-radius:8px;padding:14px 10px 0 48px}
.feature .icon{position:absolute;left:14px;top:14px;width:25px;height:25px;border-radius:6px;background:var(--green);display:flex;align-items:center;justify-content:center}
.feature h3{font-size:10px;color:var(--dark);margin-bottom:5px;white-space:nowrap}
.feature p{font-size:7px;line-height:11px;color:var(--grey)}

.mascot{position:absolute;background:var(--green);border-radius:48% 52% 40% 60%/55% 45% 55% 45%}
.blob{position:absolute;background:var(--mint);border-radius:55% 45% 60% 40%/50% 60% 40% 50%}

.card{position:absolute;background:var(--white);border-radius:10px;box-shadow:0 4px 12px rgba(0,0,0,.08);overflow:hidden}
.card-media{position:relative;width:100%}
.tag{position:absolute;right:8px;top:9px;background:var(--green);color:var(--white);font-family:var(--head);font-size:7.5px;padding:2px 8px;border-radius:10px}
.card-body{padding:9px 11px 10px}
.card h3{font-size:11px;color:var(--dark);margin-bottom:3px;white-space:nowrap}
.card p{font-size:6.5px;line-height:9px;color:var(--grey);min-height:10px}
.chips{display:flex;gap:5px;margin:6px 0 8px}
.chips span{font-size:5.5px;padding:2px 5px;border-radius:8px;background:var(--mint);color:var(--ink);white-space:nowrap}
.actions{display:flex;align-items:center;gap:8px}
.more{flex:1;height:15px;border:1px solid #ddd;border-radius:10px;font-family:var(--head);font-size:7px;color:var(--grey);display:flex;align-items:center;justify-content:center}
.add{width:16px;height:16px;border-radius:50%;background:var(--green);display:flex;align-items:center;justify-content:center}

.quote{position:absolute;width:410px}
.quote .mark{position:absolute;width:36px;height:36px;border-radius:50%;background:var(--mint);color:var(--green);font-family:var(--head);font-size:14px;display:flex;align-items:center;justify-content:center}
.stars{color:var(--green);font-size:8px;letter-spacing:2px}
.quote blockquote{font-style:italic;font-size:8.5px;line-height:13px;color:var(--ink);margin:4px 0 9px}
.quote cite{font-style:normal;font-size:6.5px;color:var(--grey)}
.quote cite b{color:var(--ink)}

.footer{position:absolute;left:0;width:601px;background:var(--dark);color:var(--white)}
.footer-brand{position:absolute;left:6px;top:18px;width:130px;height:46px;border:2px solid var(--white);display:flex;align-items:center;justify-content:center;font-family:var(--head);font-size:17px;letter-spacing:1px}
.footer p,.footer li{font-size:7px;line-height:13px;color:#e6e6e6;list-style:none}
.footer h4{font-family:var(--head);font-weight:400;font-size:9px;color:var(--green);margin-bottom:8px}
.social{display:flex;gap:8px}
.social span{width:17px;height:17px;border-radius:50%;background:var(--grey);display:block}

.overlay{position:absolute;left:601px;top:37px;width:601px;height:260px;background:#2e2e2e;overflow:hidden}
.drawer{position:absolute;left:400px;top:0;width:198px;height:260px;background:var(--white);padding:11px 11px}
.drawer h2{font-size:11px;color:var(--dark);margin-bottom:12px}
.label{font-family:var(--head);font-size:6px;color:var(--grey);letter-spacing:.4px}

.chip{position:absolute;top:325px;height:27px;border-radius:8px;background:var(--mint);display:flex;align-items:center;gap:5px;padding:0 7px}
.chip small{display:block;font-size:5px;color:var(--grey)}
.chip b{display:block;font-size:6.5px;color:var(--ink)}
.step{position:absolute;width:180px;height:24px;background:var(--white);border-radius:6px;box-shadow:0 2px 6px rgba(0,0,0,.05);font-size:6.5px;font-weight:600;padding:8px 8px;color:var(--ink)}
.dot{position:absolute;width:20px;height:20px;border-radius:50%;background:var(--green);color:var(--white);font-family:var(--head);font-size:8px;display:flex;align-items:center;justify-content:center}
.faq{position:absolute;left:1337px;width:333px;height:27px;border:1px solid #e4e4e4;border-radius:6px;font-family:var(--head);font-size:7.5px;color:var(--dark);padding:9px 11px;display:flex;justify-content:space-between}
</style>
</head>
<body>
<div class="stage">

<section class="screen" style="left:0;height:2044px">
  <header class="nav">
    <div class="brand">VELUMO</div>
    <nav class="nav-links"><span>HOME</span><span>ACTIVITEITEN</span><span>OVER ONS</span><span>CONTACT</span></nav>
    <span class="nav-lang">NL ▾</span>
    <svg class="nav-cart" width="10" height="10" viewBox="0 0 24 24" fill="none" stroke="#646463" stroke-width="2"><path d="M3 4h3l2 11h11l2-8H7"/><circle cx="10" cy="20" r="1.5"/><circle cx="18" cy="20" r="1.5"/></svg>
  </header>

  <div class="hero" style="top:37px;height:223px">
    <div class="hero-photo" role="img" aria-label="Groepsfoto van een springend team op een grasveld" style="background:linear-gradient(160deg,#7f9a4f 0%,#5f7a3c 45%,#6c8848 100%)"></div>
    <h1 class="hero-title" style="top:50px">Teambuilding met<br>een twist!</h1>
    <p class="abs" style="top:125px;left:0;width:601px;text-align:center;color:#f2f2f2;font-size:10.5px">Onvergetelijke teambuildingactiviteiten op maat van jouw team</p>
    <span class="pill abs" style="left:196px;top:157px;width:212px;height:20px">ONTDEK ONZE ACTIVITEITEN</span>
    <svg class="abs" style="left:305px;top:199px" width="10" height="7" viewBox="0 0 10 7" fill="none" stroke="#fff" stroke-width="1.2"><path d="M1 1l4 4 4-4"/></svg>
  </div>

  <div class="blob" style="left:490px;top:322px;width:130px;height:110px"></div>
  <h2 class="section-title" style="top:354px">Waarom Velumo?</h2>

  <div class="feature" style="left:70px;top:406px"><span class="icon"><svg width="12" height="12" viewBox="0 0 24 24" fill="none" stroke="#fff" stroke-width="2"><path d="M4 12h6V6h4v6h6"/></svg></span><h3>Op maat gemaakt</h3><p>Elk pakket wordt aangepast aan jouw team en wensen</p></div>
  <div class="feature" style="left:310px;top:406px"><span class="icon"><svg width="12" height="12" viewBox="0 0 24 24" fill="none" stroke="#fff" stroke-width="2"><circle cx="12" cy="12" r="4"/><path d="M12 2v3M12 19v3M2 12h3M19 12h3"/></svg></span><h3>Indoor &amp; Outdoor</h3><p>Activiteiten voor elk seizoen en elke locatie</p></div>
  <div class="feature" style="left:70px;top:498px"><span class="icon"><svg width="12" height="12" viewBox="0 0 24 24" fill="none" stroke="#fff" stroke-width="2"><circle cx="9" cy="8" r="3"/><path d="M3 20c0-4 3-6 6-6s6 2 6 6"/><circle cx="17" cy="9" r="2"/></svg></span><h3>Voor elk team</h3><p>Van 10 tot 200+ deelnemers, wij passen ons aan</p></div>
  <div class="feature" style="left:310px;top:498px"><span class="icon"><svg width="12" height="12" viewBox="0 0 24 24" fill="none" stroke="#fff" stroke-width="2"><path d="M12 3l2.7 5.6 6.1.8-4.4 4.3 1 6.1L12 17l-5.4 2.8 1-6.1L3.2 9.4l6.1-.8z"/></svg></span><h3 style="font-size:9.5px">Professionele begeleiding</h3><p>Ervaren animatoren zorgen voor een vlekkeloos verloop</p></div>

  <svg class="abs" style="left:0;top:620px" width="601" height="680" viewBox="0 0 601 680" preserveAspectRatio="none"><path d="M0 22 C150 4 420 34 601 10 V660 C420 680 150 652 0 674Z" fill="#f5f5f3"/></svg>
  <div class="mascot" role="img" aria-label="Mascotte-vorm" style="left:452px;top:600px;width:106px;height:110px"></div>
  <h2 class="section-title" style="top:718px">Onze activiteiten</h2>

  <article class="card" style="left:40px;top:770px;width:164px">
    <div class="card-media" role="img" aria-label="Team speelt samen op Afrikaanse trommels" style="height:123px;background:linear-gradient(160deg,#6b4a33,#3d2a1e)"><span class="tag">Vanaf €35/pp</span></div>
    <div class="card-body"><h3>Drum Rush</h3><p>Muzikale teambuilding met Afrikaanse drums</p><div class="chips"><span>2-3u</span><span>10-200 personen</span><span>⌂●</span></div><div class="actions"><span class="more">MEER INFO</span><span class="add"><svg width="8" height="8" viewBox="0 0 24 24" fill="none" stroke="#fff" stroke-width="2.5"><path d="M3 4h3l2 11h11l2-8H7"/></svg></span></div></div>
  </article>
  <article class="card" style="left:220px;top:770px;width:163px">
    <div class="card-media" role="img" aria-label="Spelers in een neonverlichte escape-ruimte" style="height:123px;background:linear-gradient(160deg,#1f2d52,#4a2a6a)"><span class="tag">Vanaf €40/pp</span></div>
    <div class="card-body"><h3>De Codekamer</h3><p>Kraak de code en ontsnap als team</p><div class="chips"><span>2-3u</span><span>10-150 personen</span><span>⌂</span></div><div class="actions"><span class="more">MEER INFO</span><span class="add"><svg width="8" height="8" viewBox="0 0 24 24" fill="none" stroke="#fff" stroke-width="2.5"><path d="M3 4h3l2 11h11l2-8H7"/></svg></span></div></div>
  </article>
  <article class="card" style="left:401px;top:770px;width:163px">
    <div class="card-media" role="img" aria-label="Team in klimhelmen in het bos" style="height:123px;background:linear-gradient(160deg,#7d9463,#4f6540)"><span class="tag">Vanaf €45/pp</span></div>
    <div class="card-body"><h3>Expeditie Eiland</h3><p>Overleven als team in de natuur</p><div class="chips"><span>3-4u</span><span>20-200 personen</span><span>●</span></div><div class="actions"><span class="more">MEER INFO</span><span class="add"><svg width="8" height="8" viewBox="0 0 24 24" fill="none" stroke="#fff" stroke-width="2.5"><path d="M3 4h3l2 11h11l2-8H7"/></svg></span></div></div>
  </article>
  <article class="card" style="left:40px;top:1008px;width:164px">
    <div class="card-media" role="img" aria-label="Touwtrekken op een zonnig sportveld" style="height:123px;background:linear-gradient(160deg,#a9c1d6,#8aa065)"><span class="tag">Vanaf €35/pp</span></div>
    <div class="card-body"><h3>Olympiade</h3><p>Sportieve teamcompetitie vol fun</p><div class="chips"><span>2-4u</span><span>20-300 personen</span><span>●</span></div><div class="actions"><span class="more">MEER INFO</span><span class="add"><svg width="8" height="8" viewBox="0 0 24 24" fill="none" stroke="#fff" stroke-width="2.5"><path d="M3 4h3l2 11h11l2-8H7"/></svg></span></div></div>
  </article>
  <article class="card" style="left:220px;top:1008px;width:164px">
    <div class="card-media" role="img" aria-label="Kleurrijke cocktails aan een bar" style="height:123px;background:linear-gradient(160deg,#5a3e2b,#c98a3a)"><span class="tag">Vanaf €45/pp</span></div>
    <div class="card-body"><h3>Cocktail Workshop</h3><p>Shake, stir &amp; geniet samen</p><div class="chips"><span>1.5-2u</span><span>10-100 personen</span><span>⌂</span></div><div class="actions"><span class="more">MEER INFO</span><span class="add"><svg width="8" height="8" viewBox="0 0 24 24" fill="none" stroke="#fff" stroke-width="2.5"><path d="M3 4h3l2 11h11l2-8H7"/></svg></span></div></div>
  </article>
  <article class="card" style="left:401px;top:1008px;width:164px">
    <div class="card-media" role="img" aria-label="Gasten in avondkledij bij een mysteriediner" style="height:123px;background:linear-gradient(160deg,#2a2d5a,#141628)"><span class="tag">Vanaf €50/pp</span></div>
    <div class="card-body"><h3>Murder Party</h3><p>Los het mysterie op als team</p><div class="chips"><span>2-3u</span><span>15-150 personen</span><span>⌂</span></div><div class="actions"><span class="more">MEER INFO</span><span class="add"><svg width="8" height="8" viewBox="0 0 24 24" fill="none" stroke="#fff" stroke-width="2.5"><path d="M3 4h3l2 11h11l2-8H7"/></svg></span></div></div>
  </article>

  <div class="mascot" role="img" aria-label="Mascotte-vorm" style="left:38px;top:1240px;width:108px;height:110px"></div>
  <h2 class="section-title" style="top:1364px">Wat onze klanten zeggen</h2>

  <div class="quote" style="left:128px;top:1414px"><span class="mark" style="left:-58px;top:12px">”</span><div class="stars">★★★★★</div><blockquote>"Fantastische ervaring! Het hele team was enthousiast. Velumo zorgde voor een vlekkeloze organisatie."</blockquote><cite><b>Sarah D.</b> — Telvora</cite></div>
  <div class="quote" style="left:68px;top:1492px;text-align:right"><span class="mark" style="left:430px;top:12px">”</span><div class="stars">★★★★★</div><blockquote>"De Drum Rush was het hoogtepunt van ons teamweekend. Professioneel, energiek en ontzettend leuk!"</blockquote><cite><b>Marc V.</b> — Marsden &amp; Co</cite></div>
  <div class="quote" style="left:128px;top:1570px"><span class="mark" style="left:-58px;top:12px">”</span><div class="stars">★★★★★</div><blockquote>"Van begin tot eind perfect geregeld. Onze collega's praten er nog steeds over. Absolute aanrader!"</blockquote><cite><b>Lisa B.</b> — Brabant Nova Bank</cite></div>
  <div class="blob" style="left:-40px;top:1610px;width:106px;height:80px"></div>

  <svg class="abs" style="left:0;top:1696px" width="601" height="225" viewBox="0 0 601 225" preserveAspectRatio="none"><path d="M0 18 C200 -4 400 -4 601 18 V225 H0Z" fill="#afca0a"/><path d="M0 26 C200 24 400 26 601 26 V32 C400 30 200 30 0 34Z" fill="#504f4f"/></svg>
  <div class="abs" style="left:516px;top:1742px;width:72px;height:74px;border-radius:50% 40% 55% 45%;background:rgba(255,255,255,.16)"></div>
  <div class="abs" style="left:18px;top:1848px;width:58px;height:58px;border-radius:45% 55% 50% 50%;background:rgba(255,255,255,.16)"></div>
  <h2 class="section-title" style="top:1781px;color:var(--white)">Klaar om te boeken?</h2>
  <p class="abs" style="left:0;top:1817px;width:601px;text-align:center;font-size:8.5px;color:var(--white)">Neem contact op en wij stellen het perfecte programma samen</p>
  <span class="abs" style="left:224px;top:1847px;width:157px;height:21px;border-radius:12px;background:var(--white)"></span>

  <footer class="footer" style="top:1917px;height:127px">
    <div class="footer-brand">VELUMO</div>
    <p class="abs" style="left:6px;top:72px;width:170px">Teambuilding met een twist! Onvergetelijke ervaringen op maat van jouw team.</p>
    <div class="abs" style="left:210px;top:40px"><h4>Contact</h4><ul><li>✉ info@velumo.be</li><li>☏ +32 (0)XX XX XX XX</li><li>⌖ België</li></ul></div>
    <div class="abs" style="left:416px;top:40px"><h4>Volg ons</h4><div class="social"><span></span><span></span><span></span></div></div>
    <div class="abs" style="left:0;top:122px;width:601px;height:5px;background:#3c3b3b"></div>
  </footer>
</section>

<section class="overlay">
  <div class="abs" style="left:8px;top:7px;width:66px;height:22px;background:#3a3a3a;color:#777;font-family:var(--head);font-size:8px;display:flex;align-items:center;justify-content:center">VELUMO</div>
  <div class="abs" style="left:190px;top:14px;font-family:var(--head);font-size:7px;color:#666;display:flex;gap:14px"><span>HOME</span><span>ACTIVITEITEN</span><span>OVER ONS</span><span>CONTACT</span></div>
  <div class="abs" style="left:42px;top:35px;width:158px;height:190px;border-radius:9px;background:#3a3a3a;overflow:hidden"><div role="img" aria-label="Trommelsessie, gedimd" style="height:100px;background:#3b2d24"></div><div style="padding:8px;font-family:var(--head);font-size:9px;color:#777">Drum Rush</div></div>
  <div class="abs" style="left:216px;top:35px;width:158px;height:190px;border-radius:9px;background:#3a3a3a;overflow:hidden"><div role="img" aria-label="Escape-ruimte, gedimd" style="height:100px;background:#222a3c"></div><div style="padding:8px;font-family:var(--head);font-size:9px;color:#777">De Codekamer</div></div>
  <aside class="drawer">
    <h2>Winkelmand</h2>
    <div class="label">ACTIVITEITEN</div>
    <div style="position:relative;margin-top:6px;height:34px;border:1px solid #eee;border-radius:6px;padding:4px 5px 0 38px">
      <div role="img" aria-label="Bosactiviteit" style="position:absolute;left:5px;top:4px;width:28px;height:25px;border-radius:4px;background:linear-gradient(160deg,#7d9463,#4f6540)"></div>
      <div style="font-size:5.5px;font-weight:600">Expeditie Eiland</div>
      <div style="font-size:5px;color:var(--grey)">€45/pp × 10 personen</div>
      <div style="font-size:5px;color:var(--green)">€450</div>
      <svg style="position:absolute;right:6px;top:12px" width="6" height="7" viewBox="0 0 12 14" fill="none" stroke="#999" stroke-width="1.5"><path d="M1 3h10M3 3v10h6V3M5 1h2"/></svg>
    </div>
    <div style="display:flex;justify-content:space-between;margin-top:14px"><span class="label">CADEAUBONNEN</span><span style="font-size:5.5px;color:var(--green)">+ Cadeaubon toevoegen</span></div>
    <div style="height:1px;background:#eee;margin:8px 0 8px"></div>
    <div style="display:flex;justify-content:space-between;align-items:center"><span style="font-family:var(--head);font-size:7.5px">Totaal</span><span style="font-family:var(--head);font-size:12px;color:var(--green)">€450</span></div>
    <span class="pill" style="width:175px;height:20px;margin-top:8px">OFFERTE AANVRAGEN</span>
  </aside>
</section>

<section class="screen" style="left:1202px;height:1365px">
  <header class="nav" style="top:2px">
    <div class="brand">VELUMO</div>
    <nav class="nav-links"><span>HOME</span><span>ACTIVITEITEN</span><span>OVER ONS</span><span>CONTACT</span></nav>
    <span class="nav-lang">NL ▾</span>
    <svg class="nav-cart" width="10" height="10" viewBox="0 0 24 24" fill="none" stroke="#646463" stroke-width="2"><path d="M3 4h3l2 11h11l2-8H7"/><circle cx="10" cy="20" r="1.5"/><circle cx="18" cy="20" r="1.5"/></svg>
  </header>
  <div class="hero" style="top:38px;height:159px">
    <div class="hero-photo" role="img" aria-label="Team met klimhelmen in een bos" style="background:linear-gradient(180deg,#7f9768 0%,#5d7049 55%,#3e4a34 100%)"></div>
    <p class="abs" style="left:8px;top:81px;font-size:6.5px;color:#eee">← Terug naar activiteiten</p>
    <h1 class="abs" style="left:7px;top:96px;font-size:28px;line-height:32px;color:var(--white);white-space:nowrap">Expeditie Eiland</h1>
    <p class="abs" style="left:7px;top:131px;font-size:8px;color:#eee">Overleven als team in de natuur</p>
  </div>

  <p class="abs" style="left:70px;top:284px;width:465px;font-size:8px;line-height:13px;color:var(--ink)">Geïnspireerd op het populaire TV-programma! Teams strijden tegen elkaar in uitdagende outdoor proeven: vlotten bouwen, oriëntatie, survival skills en meer. Wie overleeft alle proeven en wint de Expeditie?</p>
  <div class="chip" style="left:70px"><span style="color:var(--green);font-size:9px">◷</span><span><small>Duur</small><b>3-4u</b></span></div>
  <div class="chip" style="left:120px"><span style="color:var(--green);font-size:9px">☺</span><span><small>Groepsgrootte</small><b>20-200</b></span></div>
  <div class="chip" style="left:191px"><span style="color:var(--green);font-size:9px">ϟ</span><span><small>Moeilijkheid</small><b>Uitdagend</b></span></div>
  <div class="chip" style="left:258px"><span style="color:var(--green);font-size:9px">⌖</span><span><small>Locatie</small><b>Outdoor</b></span></div>
  <div class="abs" style="left:70px;top:367px;width:463px;height:43px;border-radius:8px;background:var(--mint);border:1px solid var(--green-soft)">
    <span class="abs head" style="left:12px;top:14px;font-size:13px;color:var(--green)">Vanaf €45/pp</span>
    <span class="pill abs" style="left:259px;top:12px;width:193px;height:19px;font-size:6.5px;letter-spacing:.3px">🛒 TOEVOEGEN AAN WINKELMAND</span>
  </div>

  <div class="abs" style="left:0;top:455px;width:601px;height:280px;background:var(--paper)"></div>
  <div class="mascot" role="img" aria-label="Mascotte-vorm" style="left:472px;top:420px;width:110px;height:112px"></div>
  <h2 class="section-title" style="top:498px;font-size:19px">Hoe werkt het?</h2>
  <div class="abs" style="left:302px;top:545px;width:1px;height:136px;background:#ddd"></div>
  <span class="dot" style="left:285px;top:542px">1</span><div class="step" style="left:316px;top:540px">Teamindeling &amp; strategie</div>
  <span class="dot" style="left:299px;top:582px">2</span><div class="step" style="left:105px;top:580px">Survival proeven</div>
  <span class="dot" style="left:285px;top:621px">3</span><div class="step" style="left:316px;top:619px">Eilandraad</div>
  <span class="dot" style="left:299px;top:661px">4</span><div class="step" style="left:105px;top:659px">Finale &amp; winnaar</div>

  <h2 class="section-title" style="top:779px;font-size:19px">Veelgestelde vragen</h2>
  <div class="faq" style="left:135px;top:818px"><span>Moet ik sportief zijn?</span><span>⌄</span></div>
  <div class="faq" style="left:135px;top:850px"><span>Wat als het regent?</span><span>⌄</span></div>

  <div class="abs" style="left:0;top:920px;width:601px;height:317px;background:var(--paper)"></div>
  <div class="mascot" role="img" aria-label="Mascotte-vorm" style="left:16px;top:874px;width:110px;height:110px"></div>
  <h2 class="section-title" style="top:946px;font-size:19px">Misschien ook interessant</h2>

  <article class="card" style="left:70px;top:986px;width:145px">
    <div class="card-media" role="img" aria-label="Team speelt samen op trommels" style="height:110px;background:linear-gradient(160deg,#6b4a33,#3d2a1e)"><span class="tag">Vanaf €35/pp</span></div>
    <div class="card-body"><h3>Drum Rush</h3><p>Muzikale teambuilding met Afrikaanse drums</p><div class="chips"><span>2-3u</span><span>10-200 personen</span><span>⌂●</span></div><div class="actions"><span class="more">MEER INFO</span><span class="add"><svg width="8" height="8" viewBox="0 0 24 24" fill="none" stroke="#fff" stroke-width="2.5"><path d="M3 4h3l2 11h11l2-8H7"/></svg></span></div></div>
  </article>
  <article class="card" style="left:229px;top:986px;width:145px">
    <div class="card-media" role="img" aria-label="Escape-ruimte met neonlicht" style="height:110px;background:linear-gradient(160deg,#1f2d52,#4a2a6a)"><span class="tag">Vanaf €40/pp</span></div>
    <div class="card-body"><h3>De Codekamer</h3><p>Kraak de code en ontsnap als team</p><div class="chips"><span>2-3u</span><span>10-150 personen</span><span>⌂</span></div><div class="actions"><span class="more">MEER INFO</span><span class="add"><svg width="8" height="8" viewBox="0 0 24 24" fill="none" stroke="#fff" stroke-width="2.5"><path d="M3 4h3l2 11h11l2-8H7"/></svg></span></div></div>
  </article>
  <article class="card" style="left:388px;top:986px;width:145px">
    <div class="card-media" role="img" aria-label="Touwtrekken op een sportveld" style="height:110px;background:linear-gradient(160deg,#a9c1d6,#8aa065)"><span class="tag">Vanaf €35/pp</span></div>
    <div class="card-body"><h3>Olympiade</h3><p>Sportieve teamcompetitie vol fun</p><div class="chips"><span>2-4u</span><span>20-300 personen</span><span>●</span></div><div class="actions"><span class="more">MEER INFO</span><span class="add"><svg width="8" height="8" viewBox="0 0 24 24" fill="none" stroke="#fff" stroke-width="2.5"><path d="M3 4h3l2 11h11l2-8H7"/></svg></span></div></div>
  </article>

  <footer class="footer" style="top:1237px;height:128px">
    <div class="footer-brand" style="top:6px">VELUMO</div>
    <p class="abs" style="left:6px;top:58px;width:170px">Teambuilding met een twist! Onvergetelijke ervaringen op maat van jouw team.</p>
    <div class="abs" style="left:210px;top:30px"><h4>Contact</h4><ul><li>✉ info@velumo.be</li><li>☏ +32 (0)XX XX XX XX</li><li>⌖ België</li></ul></div>
    <div class="abs" style="left:416px;top:30px"><h4>Volg ons</h4><div class="social"><span></span><span></span><span></span></div></div>
    <div class="abs" style="left:0;top:123px;width:601px;height:5px;background:#3c3b3b"></div>
  </footer>
</section>

</div>
</body>
</html>
```